Tallow Crest Business Card

We need a business card designed for a a company called "Tallow Crest". We offer consulting, coaching and training to business leaders and coaches (across the world) using the latest findings in neuroscience, social and emotional intelligence and positive psychology. The final design should communicate the use of brain science to create sustainable relationships.

The card should be doublesided. The logo is attached and names and titles will be provided to the successful designer. Thank you.

Industry/Entity Type

Training

```html
<!DOCTYPE html>
<html lang="en">
<head>
<meta charset="utf-8">
<title>Tallow Crest Business Card</title>
<link rel="stylesheet" href="https://fonts.googleapis.com/css2?family=Ubuntu:wght@400;500;700&display=swap">
<style>
  :root {
    --page: #2a2a2a;
    --card: #eceef0;
    --ink: #5f6163;
    --brand-blue: #3f9fd8;
    --soft-blue: #a9d2ea;
    --soft-green: #d9e6a6;
    --tab: #1f1f20;
    --oval: #ffffff;
  }
  * { box-sizing: border-box; margin: 0; padding: 0; }
  html, body { width: 1200px; height: 1000px; overflow: hidden; }
  body {
    background: var(--page);
    font-family: "Ubuntu", sans-serif;
    position: relative;
  }
  .card {
    position: absolute;
    top: 200px;
    width: 400px;
    height: 600px;
    background: var(--card);
    overflow: hidden;
  }
  .card--back { left: 150px; }
  .card--front { left: 650px; }

  .symbol-area {
    position: absolute;
    left: 20px; top: 20px;
    width: 360px; height: 300px;
    background: linear-gradient(90deg, var(--soft-blue) 0%, #c6dfe4 50%, var(--soft-green) 100%);
    opacity: 0.75;
    border-radius: 6px;
  }

  .contact-oval {
    position: absolute;
    left: 50px; top: 70px;
    width: 300px; height: 200px;
    border-radius: 50%;
    background: var(--oval);
    box-shadow: 0 0 0 6px #f6f7f8, 0 2px 8px rgba(0,0,0,0.12);
    display: flex;
    flex-direction: column;
    align-items: center;
    justify-content: center;
    gap: 4px;
    color: var(--ink);
    text-align: center;
  }
  .contact-oval .company { color: var(--brand-blue); font-weight: 700; font-size: 15px; margin-bottom: 8px; text-transform: uppercase; }
  .contact-oval .tel { font-size: 18px; font-weight: 500; }
  .contact-oval .address { font-size: 12px; }
  .contact-oval .postcode { font-size: 17px; font-weight: 700; }
  .contact-oval .email { font-size: 15px; font-weight: 500; }
  .contact-oval .website { font-size: 13px; font-weight: 500; }

  .word-rows {
    position: absolute;
    left: 0; right: 0; top: 380px;
    color: var(--soft-blue);
    font-weight: 700;
    white-space: nowrap;
    text-transform: uppercase;
    line-height: 1;
  }
  .word-rows .row-small { font-size: 16px; letter-spacing: 1px; padding-left: 8px; }
  .word-rows .row-medium { font-size: 30px; letter-spacing: 1px; padding-left: 8px; margin-top: 6px; }
  .word-rows .row-large { font-size: 112px; letter-spacing: 4px; padding-left: 6px; margin-top: 8px; }

  .brand-tab {
    position: absolute;
    left: 0; top: 40px;
    width: 200px; height: 130px;
    background: var(--tab);
    border-radius: 0 20px 20px 0;
    display: flex;
    align-items: center;
    justify-content: center;
    gap: 10px;
  }
  .brand-tab .mark-square { width: 18px; height: 18px; background: var(--brand-blue); }
  .brand-tab .brand-name { color: var(--brand-blue); font-weight: 700; font-size: 23px; }

  .corner-shape { position: absolute; right: 0; top: 190px; width: 110px; height: 170px; }
</style>
</head>
<body>
  <section class="card card--back" aria-label="Card back">
    <div class="symbol-area" role="img" aria-label="Faint brand symbol decoration in soft blue and green"></div>
    <div class="contact-oval">
      <p class="company">Tallow Crest</p>
      <p class="tel">tel: 48 20 7391</p>
      <p class="address">Ad:Harrow Lane 23</p>
      <p class="postcode">P.C.: 00000</p>
      <p class="email">e-mail:info@tallowcrest.com</p>
      <p class="website">website:www.tallowcrest.com</p>
    </div>
    <div class="word-rows" aria-hidden="true">
      <p class="row-small">Crest Crest Crest Crest Crest Crest Crest</p>
      <p class="row-medium">Crest Crest Crest Crest</p>
      <p class="row-large">Crest</p>
    </div>
  </section>

  <section class="card card--front" aria-label="Card front">
    <div class="symbol-area" role="img" aria-label="Faint brand symbol decoration in soft blue and green"></div>
    <div class="brand-tab">
      <span class="mark-square"></span>
      <span class="brand-name">Tallow Crest</span>
    </div>
    <svg class="corner-shape" viewBox="0 0 110 170" aria-hidden="true">
      <path d="M110 0 L110 170 L18 170 Q0 170 8 152 L88 14 Q96 0 110 0 Z" fill="#1f1f20"/>
    </svg>
    <div class="word-rows" aria-hidden="true">
      <p class="row-small">Crest Crest Crest Crest Crest Crest Crest</p>
      <p class="row-medium">Crest Crest Crest Crest</p>
      <p class="row-large">Crest</p>
    </div>
  </section>
</body>
</html>
```